eBook front and back cover

I'm releasing an brindle ebook with dimensions 2,560 x 1,600 pixels, I need the following Text:

Title: How to Shape a Standout Lectern Talk Review
Subtitle: Using feedback to nurture, grow and ignite every speaker
Author: Martin Oakes-Whitby

Text Colour options: #770F2A, #FFEB88, #003F62, #FFFFFF, #000000

Image: Anything you that you choose. It needs to represent growth and development, but not cheesy or obvious. No design will win with obvious images. I want a creative design,

Back cover: Please continue the theme on the reverse and use the author photo if you like. Please leave room for 2-3 paragraphs of text and let me know any fonts that are used so I can match these later.

Style: Needs to look modern, business-like and professional. I want a white background and minimalist approach to the design.

Notes: Please do not use any trademarked images from Podium Circle Global. This is an unofficial book.

Files: I need a high-quality PDF version that is ready to upload to Brindle. I also need a 3d versions of the front and back cover with a small shadow to the right of the book. The book is about 60 pages, so please do not make the 3D version look too long.

I've attached the version that I made myself as an idea for the type of design that I want. I'm not looking for an improvement on this, just a flavour of the type of thing I'm looking for. I've also attached a number of other non-fiction covers that would like to be similar to.

Thanks very much for your help.

Target Market(s)

Professionals. People that want to improve their communication skills.

Font styles to use
Sans Serif

Requirements
Must have
• White background. Clean, modern looking interface. Professional font. Simple design, all text easy to read.
Should not have
• Too busy. Cheesy images like arrows pointing up or forward or old fashioned images of success. Shouldn't just have someone speaking or a microphone. I need the design to be more creative than that.

```html
<!DOCTYPE html>
<html lang="en">
<head>
<meta charset="UTF-8">
<title>How to Shape a Standout Lectern Talk Review — Cover</title>
<link rel="stylesheet" href="https://fonts.googleapis.com/css2?family=Playfair+Display:wght@700;800;900&family=Montserrat:wght@500;600&display=swap">
<style>
  :root {
    --page-bg: #f4f4f4;
    --cover-white: #ffffff;
    --ink-black: #0d0d0d;
    --title-gold: #e3c067;
    --flame-orange: #f08a1c;
    --flame-yellow: #ffd35a;
    --subtitle-ink: #2a2a2a;
  }
  * { margin: 0; padding: 0; box-sizing: border-box; }
  html, body {
    width: 1200px;
    height: 798px;
    overflow: hidden;
    background: var(--page-bg);
  }
  .stage {
    width: 1200px;
    height: 798px;
    display: flex;
    align-items: center;
    justify-content: center;
  }
  .cover {
    position: relative;
    width: 462px;
    height: 740px;
    background: var(--cover-white);
    box-shadow: 0 1px 3px rgba(0,0,0,0.12);
  }
  .title-block {
    position: absolute;
    top: 52px;
    left: 40px;
    right: 30px;
    height: 190px;
    background: var(--ink-black);
    display: flex;
    flex-direction: column;
    align-items: center;
    justify-content: center;
    text-align: center;
    color: var(--title-gold);
    font-family: "Playfair Display", Georgia, serif;
    font-weight: 900;
    text-transform: uppercase;
  }
  .title-block .line { display: block; font-size: 27px; line-height: 1.12; letter-spacing: 0.01em; }
  .title-block .line.wide { font-size: 28px; letter-spacing: 0.36em; margin-right: -0.36em; }
  .artwork {
    position: absolute;
    top: 275px;
    left: 105px;
    width: 260px;
    height: 235px;
    background:
      radial-gradient(ellipse 60% 45% at 50% 78%, var(--flame-yellow) 0%, var(--flame-orange) 55%, rgba(240,138,28,0.25) 80%, transparent 100%);
  }
  .subtitle {
    position: absolute;
    top: 535px;
    left: 80px;
    right: 70px;
    text-align: center;
    font-family: "Montserrat", Arial, sans-serif;
    font-weight: 600;
    font-size: 12px;
    line-height: 1.45;
    letter-spacing: 0.06em;
    text-transform: uppercase;
    color: var(--subtitle-ink);
  }
  .author-band {
    position: absolute;
    top: 628px;
    left: 40px;
    right: 30px;
    height: 56px;
    background: var(--ink-black);
    display: flex;
    align-items: center;
    justify-content: center;
    font-family: "Playfair Display", Georgia, serif;
    font-weight: 900;
    font-size: 21px;
    letter-spacing: 0.03em;
    text-transform: uppercase;
    color: var(--title-gold);
  }
</style>
</head>
<body>
  <main class="stage">
    <article class="cover">
      <h1 class="title-block">
        <span class="line">How to</span>
        <span class="line">Shape a Standout</span>
        <span class="line wide">Lectern</span>
        <span class="line">Talk Review</span>
      </h1>
      <div class="artwork" role="img" aria-label="Illustration of a line-drawn diamond rising out of orange and yellow flames"></div>
      <p class="subtitle">Using feedback to nurture,<br>grow and ignite every speaker</p>
      <p class="author-band">Martin Oakes-Whitby</p>
    </article>
  </main>
</body>
</html>
```